Tervolan Pty Ltd professional business card

A professional business card template using the colours from the supplied logo.
Clean crisp lines while, Modern while not being over the top.

Target Market(s)

Construction, commerical and industrial

Industry/Entity Type

Communications

Contact Information for Business Card

For a Communications, IT, Optical fibre installation company

Colors
37b8a4

```html
<!DOCTYPE html>
<html lang="en">
<head>
<meta charset="utf-8">
<title>Tervolan Pty Ltd – Business Card</title>
<link rel="stylesheet" href="https://fonts.googleapis.com/css2?family=Montserrat:wght@600;700&family=Noto+Sans:wght@400&display=swap">
<style>
  :root {
    --page-bg: #2b2b2d;
    --card-bg: #232325;
    --teal: #1597a6;
    --grey-text: #8a8a8d;
    --logo-grey: #707073;
    --rule: #4a4a4d;
  }
  * { margin: 0; padding: 0; box-sizing: border-box; }
  html, body {
    width: 1200px; height: 866px; overflow: hidden;
    background: var(--page-bg);
  }
  .canvas {
    width: 1200px; height: 866px;
    display: flex; flex-direction: column;
    align-items: center; justify-content: center; gap: 22px;
  }
  .card {
    position: relative;
    width: 700px; height: 400px;
    background: var(--card-bg);
    border-bottom: 12px solid var(--teal);
    box-shadow: 0 10px 24px rgba(0,0,0,.45);
    overflow: hidden;
  }
  .wordmark {
    font-family: "Montserrat", sans-serif;
    font-weight: 600;
    color: var(--logo-grey);
    letter-spacing: 4px;
    text-transform: uppercase;
    display: flex; align-items: center; gap: 14px;
  }
  .wordmark .dot {
    width: 18px; height: 18px; border-radius: 50%;
    background: var(--logo-grey);
  }
  .card--front .wordmark {
    position: absolute; left: 50%; top: 50%;
    transform: translate(-50%, -56%);
    font-size: 58px;
  }
  .card--back .wordmark {
    position: absolute; right: 48px; top: 78px;
    font-size: 38px;
  }
  .card--back .wordmark .dot { width: 13px; height: 13px; }
  .contact {
    position: absolute; left: 44px; top: 60px;
    font-family: "Noto Sans", sans-serif;
    color: var(--grey-text);
  }
  .contact__name {
    font-family: "Montserrat", sans-serif; font-weight: 700;
    color: var(--teal); font-size: 24px; letter-spacing: 1.5px;
    text-transform: uppercase;
  }
  .contact__title { font-size: 17px; margin: 2px 0 14px; }
  .contact__list { list-style: none; font-size: 16px; line-height: 25px; }
  .contact__list li { display: flex; align-items: center; gap: 10px; }
  .contact__list svg { width: 17px; height: 17px; flex: none; }
  .contact__list .accent { color: var(--teal); }
  .divider {
    position: absolute; left: 290px; right: 48px; top: 213px;
    height: 1px; background: var(--rule);
  }
  .company {
    position: absolute; right: 48px; bottom: 40px;
    text-align: right;
    font-family: "Noto Sans", sans-serif; color: var(--grey-text);
    font-size: 16px; line-height: 22px;
  }
  .company__name {
    font-family: "Montserrat", sans-serif; font-weight: 700;
    color: var(--teal); font-size: 18px; letter-spacing: 1px;
  }
</style>
</head>
<body>
<main class="canvas">
  <section class="card card--front" aria-label="Card front">
    <div class="wordmark"><span class="dot"></span>Tervolan</div>
  </section>

  <section class="card card--back" aria-label="Card back">
    <div class="contact">
      <p class="contact__name">Marcus Hale</p>
      <p class="contact__title">Managing Director</p>
      <ul class="contact__list">
        <li>
          <svg viewBox="0 0 20 20" fill="none" stroke="#8a8a8d" stroke-width="1.6"><rect x="1" y="1" width="18" height="18" rx="2"/><path d="M7 5c-1 1-1 3 1 6s4 4 5 3l1-1-2-2-1 1c-1-.5-2-2-2.5-3l1-1-2-2z" fill="#8a8a8d" stroke="none"/></svg>
          055-210 348 671
        </li>
        <li>
          <svg viewBox="0 0 20 20" fill="#8a8a8d"><rect x="5" y="1" width="10" height="6"/><rect x="1" y="7" width="18" height="8" rx="1"/><rect x="5" y="12" width="10" height="7" fill="#232325" stroke="#8a8a8d" stroke-width="1.6"/></svg>
          055-210 348 672
        </li>
        <li>
          <svg viewBox="0 0 20 20" fill="#8a8a8d"><path d="M1 4h18v12H1z"/><path d="M1 4l9 7 9-7" fill="none" stroke="#232325" stroke-width="1.6"/></svg>
          info@tervolan.net
        </li>
        <li>
          <svg viewBox="0 0 20 20" fill="none" stroke="#8a8a8d" stroke-width="1.5"><circle cx="10" cy="10" r="8.5"/><ellipse cx="10" cy="10" rx="4" ry="8.5"/><path d="M1.5 10h17M3 5.5h14M3 14.5h14"/></svg>
          <span>www.<span class="accent">tervolan</span>.net</span>
        </li>
      </ul>
    </div>
    <div class="divider"></div>
    <div class="wordmark"><span class="dot"></span>Tervolan</div>
    <address class="company" style="font-style:normal">
      <p class="company__name">Tervolan Pty Ltd</p>
      <p>48, Quarry Lane Road</p>
      <p>Northfield, 204815</p>
    </address>
  </section>
</main>
</body>
</html>
```